Succession & Estate Planning firm needs a double-sided one page client handout

We need a client hand-out that highlights the top 10 Reasons to get a Pension Plan. It will need the 10 reasons as headings, with a short description of each reason (attached Word doc). It should communicate that a Pension Plan is flexible and provides security. Our usual client is a business owner/medical professional/entrepreneur. Have a look at our website for more info about our business www.marvelko.ca Our logo colours are 83c242, 3b3839, d5d5d5 We like clean, modern, info-graphics, not too cluttered, not too loudWe would like the ability to update the text/content ourselves, in the future.

```html
<!DOCTYPE html>
<html lang="en">
<head>
<meta charset="utf-8">
<title>Top 10 Reasons – Marvelko</title>
<link href="https://fonts.googleapis.com/css2?family=Montserrat:wght@300;400;600;700&family=Oswald:wght@500&display=swap" rel="stylesheet">
<style>
:root{
  --green:#83c242;
  --dark:#3b3839;
  --grey:#d5d5d5;
  --panel:#e4e4e4;
  --icon:#8a8889;
  --backdrop:#efeeec;
  --white:#ffffff;
}
*{box-sizing:border-box;margin:0;padding:0}
html,body{width:1200px;height:1200px;overflow:hidden;background:var(--backdrop);font-family:'Montserrat',sans-serif;color:var(--dark)}
.sheet{position:absolute;width:648px;height:916px;background:var(--white);transform:scale(.8);transform-origin:0 0;overflow:hidden;box-shadow:0 2px 8px rgba(0,0,0,.12)}
.sheet--front{left:66px;top:234px}
.sheet--back{left:617px;top:234px}

.hero{position:absolute;left:0;top:0;width:648px;height:546px;
  background:
    linear-gradient(180deg,rgba(255,255,255,.9) 0%,rgba(255,255,255,.55) 22%,rgba(255,255,255,0) 45%),
    radial-gradient(ellipse at 20% 40%,#f4e6c8 0%,rgba(244,230,200,0) 45%),
    linear-gradient(180deg,#e9eddc 0%,#c9d99a 40%,#8fb04a 62%,#5d7a2c 78%,#5a4634 88%,#3e2e22 100%);}
.brand{position:absolute;left:0;right:0;top:70px;text-align:center}
.brand__name{font-weight:300;font-size:46px;letter-spacing:7px;color:var(--dark)}

.title-band{position:absolute;left:0;top:546px;width:648px;height:100px;background:var(--green);text-align:center;font-family:'Oswald',sans-serif;font-weight:500;line-height:1.15;padding-top:10px}
.title-band__top{font-size:32px;color:var(--dark)}
.title-band__main{font-size:33px;color:var(--white)}

.reason{position:absolute;display:flex}
.reason__panel{position:relative;background:var(--panel);height:100%}
.reason__tab{position:absolute;left:0;top:0;height:100%}
.reason__num{position:absolute;left:10px;bottom:6px;font-size:30px;font-weight:600;color:var(--white)}
.reason__body{position:absolute;top:10px;right:18px}
.reason__title{font-size:11px;font-weight:700;margin-bottom:5px}
.reason__text{font-size:9.4px;line-height:1.35;text-align:justify}
.reason__icon{position:absolute;top:0;height:100%;width:102px;background:var(--icon);display:flex;align-items:center;justify-content:center}
.reason__icon::before{content:"";position:absolute;left:-6px;top:50%;margin-top:-6px;border:6px solid transparent;border-left:0;border-right-color:var(--icon)}
.reason__icon svg{width:48px;height:48px;fill:none;stroke:var(--white);stroke-width:2.4;stroke-linecap:round;stroke-linejoin:round}

.front-row{left:29px;width:584px;height:76px}
.front-row .reason__panel{width:471px}
.front-row .reason__tab{width:88px}
.front-row .reason__body{left:99px}
.front-row .reason__icon{left:482px}

.back-row{left:30px;width:585px;height:87px}
.back-row .reason__panel{width:472px}
.back-row .reason__tab{width:88px}
.back-row .reason__body{left:100px}
.back-row .reason__icon{left:483px}
.back-row .reason__num{bottom:12px}

.footer{position:absolute;left:0;width:648px;background:var(--dark);color:var(--white)}
.footer--front{top:855px;height:61px}
.footer__address{position:absolute;left:34px;top:14px;font-size:13px;line-height:1.25;font-weight:600}
.footer__address svg{position:absolute;left:-22px;top:1px;width:15px;height:14px;fill:var(--green)}
.footer__band{position:absolute;background:var(--green);clip-path:polygon(0 0,100% 0,100% 100%,7% 100%)}
.footer--front .footer__band{left:286px;top:4px;width:362px;height:44px}
.footer__contact{position:absolute;font-size:13px;font-weight:600;display:flex;align-items:center;gap:7px}
.footer__contact svg{width:17px;height:17px;fill:none;stroke:var(--dark);stroke-width:1.8}
.footer--back{top:861px;height:55px}
.footer--back .footer__band{left:230px;top:3px;width:418px;height:34px;clip-path:polygon(0 0,100% 0,100% 100%,4% 100%)}
.footer__web{position:absolute;left:90px;right:0;top:9px;text-align:center;font-size:14px;letter-spacing:5px;color:var(--white)}
</style>
</head>
<body>

<section class="sheet sheet--front">
  <div class="hero" role="img" aria-label="Photo of young green seedlings growing from stacks of gold coins in soil, rising left to right against a soft sunlit meadow">
    <div class="brand">
      <div class="brand__name">MARVELKO</div>
    </div>
  </div>
  <div class="title-band">
    <div class="title-band__top">TOP 10 REASONS</div>
    <div class="title-band__main">Why an FPP Serves Your Family Enterprise</div>
  </div>

  <div class="reason front-row" style="top:665px">
    <div class="reason__panel">
      <svg class="reason__tab" viewBox="0 0 88 76" preserveAspectRatio="none"><polygon points="0,14 60,14 88,76 0,76" fill="#83c242"/></svg>
      <span class="reason__num">1</span>
      <div class="reason__body">
        <div class="reason__title">Create Significant Deductions</div>
        <div class="reason__text">The FPP creates significant tax deductions, which can be used to keep the business under the small business rate or applied to the high rate.</div>
      </div>
    </div>
    <div class="reason__icon"><svg viewBox="0 0 48 48"><rect x="6" y="10" width="34" height="22" rx="2"/><circle cx="36" cy="32" r="6"/><path d="M14 20v18M10 38h8M20 16h14"/></svg></div>
  </div>

  <div class="reason front-row" style="top:759px">
    <div class="reason__panel">
      <svg class="reason__tab" viewBox="0 0 88 76" preserveAspectRatio="none"><polygon points="0,14 60,14 88,76 0,76" fill="#83c242"/></svg>
      <span class="reason__num">2</span>
      <div class="reason__body" style="top:22px">
        <div class="reason__title">Deliberate, Planned, Future Income</div>
        <div class="reason__text">An income for beyond the last day at the office.</div>
      </div>
    </div>
    <div class="reason__icon"><svg viewBox="0 0 48 48"><rect x="4" y="8" width="40" height="34" rx="3"/><path d="M4 16h40M14 4v8M34 4v8M11 23h4M19 23h4M27 23h4M35 23h2M11 30h4M19 30h4M27 30h4M35 30h2M11 36h4M19 36h4M27 36h4"/></svg></div>
  </div>

  <footer class="footer footer--front">
    <div class="footer__address">
      <svg viewBox="0 0 16 14"><path d="M8 0L0 7h2v7h4V9h4v5h4V7h2z"/></svg>
      410 – 128 Birch Avenue<br>Saskatoon, Saskatchewan, S7K 2M4
    </div>
    <div class="footer__band"></div>
    <div class="footer__contact" style="left:320px;top:19px"><svg viewBox="0 0 18 18"><path d="M4 2l3 3-2 2c1 2 3 4 5 5l2-2 3 3-2 3C7 16 2 11 1 5z"/></svg><span>(306) 555-0142</span></div>
    <div class="footer__contact" style="left:471px;top:19px"><svg viewBox="0 0 18 18"><circle cx="9" cy="9" r="7.5"/><path d="M1.5 9h15M9 1.5c3 3 3 12 0 15M9 1.5c-3 3-3 12 0 15"/></svg><span>www.marvelko.ca</span></div>
  </footer>
</section>

<section class="sheet sheet--back">

  <div class="reason back-row" style="top:28px">
    <div class="reason__panel">
      <svg class="reason__tab" viewBox="0 0 88 87" preserveAspectRatio="none"><polygon points="0,14 60,14 88,87 0,87" fill="#83c242"/></svg>
      <span class="reason__num">3</span>
      <div class="reason__body">
        <div class="reason__title">Past Buy Back</div>
        <div class="reason__text">Most owners invest in their business first. The FPP offers the ability to go back and recover lost years when RRSP contributions were not made and pass the tax savings onto their company.</div>
      </div>
    </div>
    <div class="reason__icon"><svg viewBox="0 0 48 48"><path d="M10 14a17 17 0 1 1-3 10"/><path d="M4 12l6 3 2-6"/><path d="M24 14v10h8"/></svg></div>
  </div>

  <div class="reason back-row" style="top:130px">
    <div class="reason__panel">
      <svg class="reason__tab" viewBox="0 0 88 87" preserveAspectRatio="none"><polygon points="0,14 60,14 88,87 0,87" fill="#83c242"/></svg>
      <span class="reason__num">4</span>
      <div class="reason__body">
        <div class="reason__title">Creditor Proof</div>
        <div class="reason__text">All assets in an FPP are creditor proof. Planned pension contributions receive “super-priority” status, which ranks above the claims of secured creditors like major commercial lenders and banks.</div>
      </div>
    </div>
    <div class="reason__icon"><svg viewBox="0 0 48 48"><path d="M4 22a20 18 0 0 1 40 0z"/><path d="M24 4v18M14 22c0-8 4-16 10-18M34 22c0-8-4-16-10-18"/><circle cx="16" cy="34" r="6"/><circle cx="32" cy="34" r="6"/></svg></div>
  </div>

  <div class="reason back-row" style="top:235px">
    <div class="reason__panel">
      <svg class="reason__tab" viewBox="0 0 88 87" preserveAspectRatio="none"><polygon points="0,14 60,14 88,87 0,87" fill="#83c242"/></svg>
      <span class="reason__num">5</span>
      <div class="reason__body">
        <div class="reason__title">Flexibility</div>
        <div class="reason__text">Owners know that cash flows can swing wildly with the business cycle. An FPP offers the flexibility to flip between DB and DC accounts to conserve cash, smooth income during volatile years, and recover assets when profits improve.</div>
      </div>
    </div>
    <div class="reason__icon"><svg viewBox="0 0 48 48"><path d="M24 44V6M18 12l6-6 6 6M24 26c-6 0-12 2-18 0M10 20l-4 6 4 6M24 26c6 0 12 2 18 0M38 20l4 6-4 6"/></svg></div>
  </div>

  <div class="reason back-row" style="top:340px">
    <div class="reason__panel">
      <svg class="reason__tab" viewBox="0 0 88 87" preserveAspectRatio="none"><polygon points="0,14 60,14 88,87 0,87" fill="#83c242"/></svg>
      <span class="reason__num">6</span>
      <div class="reason__body">
        <div class="reason__title">Preserve the Lifetime Capital Gains Exemption</div>
        <div class="reason__text">Create $1.6 Million+ of Tax Free Capital Gains. The significant deductions created in an FPP can be used to purify a corporation with passive assets, which can help preserve the shareholders’ lifetime capital gains exemption.</div>
      </div>
    </div>
    <div class="reason__icon"><svg viewBox="0 0 48 48"><rect x="10" y="22" width="30" height="18"/><path d="M6 36V18h30"/><circle cx="25" cy="31" r="4"/><path d="M28 14v4M32 11v7M36 8v10M40 5v13"/></svg></div>
  </div>

  <div class="reason back-row" style="top:445px">
    <div class="reason__panel">
      <svg class="reason__tab" viewBox="0 0 88 87" preserveAspectRatio="none"><polygon points="0,14 60,14 88,87 0,87" fill="#83c242"/></svg>
      <span class="reason__num">7</span>
      <div class="reason__body">
        <div class="reason__title">Intergenerational Wealth Transfer</div>
        <div class="reason__text">Unlike RRSPs that eventually trigger a taxable disposition upon death, an FPP has the ability to pass, tax deferred, to the next generation of family business owners.</div>
      </div>
    </div>
    <div class="reason__icon"><svg viewBox="0 0 48 48"><rect x="6" y="16" width="36" height="16" rx="2"/><circle cx="24" cy="24" r="4"/><path d="M30 10H16M20 6l-4 4 4 4M18 38h14M28 34l4 4-4 4"/></svg></div>
  </div>

  <div class="reason back-row" style="top:550px">
    <div class="reason__panel">
      <svg class="reason__tab" viewBox="0 0 88 87" preserveAspectRatio="none"><polygon points="0,14 60,14 88,87 0,87" fill="#83c242"/></svg>
      <span class="reason__num">8</span>
      <div class="reason__body" style="top:24px">
        <div class="reason__title">All Ages</div>
        <div class="reason__text">An FPP can benefit all entrepreneurs between ages 18-71.</div>
      </div>
    </div>
    <div class="reason__icon"><svg viewBox="0 0 48 48"><circle cx="7" cy="14" r="3"/><path d="M4 20h6v18M7 28v10"/><circle cx="18" cy="16" r="3"/><path d="M15 22h6v16"/><circle cx="30" cy="16" r="3"/><path d="M27 22h6v16"/><circle cx="41" cy="14" r="3"/><path d="M38 20h6v18"/></svg></div>
  </div>

  <div class="reason back-row" style="top:655px">
    <div class="reason__panel">
      <svg class="reason__tab" viewBox="0 0 88 87" preserveAspectRatio="none"><polygon points="0,14 60,14 88,87 0,87" fill="#83c242"/></svg>
      <span class="reason__num">9</span>
      <div class="reason__body">
        <div class="reason__title">Conserve the Small Business Deduction</div>
        <div class="reason__text">Investment income inside an FPP grows tax exempt and does not create passive income. Business owners that redirect corporate resources to fund their pension assets will not jeopardize their low corporate tax rate on profits and in associated companies.</div>
      </div>
    </div>
    <div class="reason__icon"><svg viewBox="0 0 48 48"><circle cx="26" cy="16" r="12"/><path d="M29 11h-4a2.5 2.5 0 0 0 0 5h2a2.5 2.5 0 0 1 0 5h-5M26 8v3M26 21v3"/><path d="M4 36h10l8 4h12l10-8-4-2-8 4h-8"/></svg></div>
  </div>

  <div class="reason back-row" style="top:760px">
    <div class="reason__panel">
      <svg class="reason__tab" viewBox="0 0 88 87" preserveAspectRatio="none"><polygon points="0,14 60,14 88,87 0,87" fill="#83c242"/></svg>
      <span class="reason__num" style="font-size:28px">10</span>
      <div class="reason__body">
        <div class="reason__title">Broader Investment Options</div>
        <div class="reason__text">An FPP allows entrepreneurs to invest in what they like: real estate, other businesses and/or franchises, private equity, public equity, exempt markets, etc.</div>
      </div>
    </div>
    <div class="reason__icon"><svg viewBox="0 0 48 48"><path d="M6 42V32M14 42V26M22 42V28M30 42V20M38 42V14"/><path d="M4 24l10-8 8 4 18-14"/><path d="M34 6h6v6"/></svg></div>
  </div>

  <footer class="footer footer--back">
    <div class="footer__band"></div>
    <div class="footer__contact" style="left:40px;top:14px;font-size:18px;font-weight:400"><svg viewBox="0 0 18 18" style="stroke:#fff"><path d="M4 2l3 3-2 2c1 2 3 4 5 5l2-2 3 3-2 3C7 16 2 11 1 5z"/></svg><span>(306) 555-0142</span></div>
    <div class="footer__web" style="left:260px">www.marvelko.ca</div>
  </footer>
</section>

</body>
</html>
```